Handy man Company business card

need branded business card for my new company, this design will transfer to car wrap design what winner will be asked to design

I will need original file so I can edit it in the end.

Also like to have some inspirational quote like "ONE CALL WE DO IT ALL"
"We do it right" can be added to logo side

Like to try to see large 1 800 000 0000 number on front with large logo

Size bigger then standard business card

I like to integrate LAS VEGAS sign to one of sides

Target Market(s)

Handy man services, Home renovation and remodeling

Industry/Entity Type

Handyman

Contact Information for Business Card

Tool Baron LLC.
Name: BORIS LENKOVA
Phone "Temporary": 000 000 0000
Adress: 2715 Fenmore Ct, Las Vegas NV 89147
Website: www.toolbaron.vegas
Email: info@toolbaron.vegas

Requirements
Must have
• Two side
• side n1: LOGO
• side n2: INFO
Nice to have
• Like to have some interesting idea for client to remember!
• With logo added to both side at different stile
Should not have
• Standard design,

```html
<!DOCTYPE html>
<html lang="en">
<head>
<meta charset="utf-8">
<title>Tool Baron – Business Card</title>
<link href="https://fonts.googleapis.com/css2?family=Open+Sans:wght@400;600;700;800&display=swap" rel="stylesheet">
<style>
  :root {
    --ink: #1f2c38;
    --amber: #f2b029;
    --amber-deep: #e8991f;
    --paper: #ffffff;
    --backdrop: #5a5850;
    --mascot-blue: #8cc3e8;
    --mascot-orange: #f0a82a;
  }
  * { box-sizing: border-box; margin: 0; padding: 0; }
  html, body {
    width: 1200px; height: 900px; overflow: hidden;
    background: var(--backdrop);
    font-family: "Open Sans", Arial, sans-serif;
  }
  .canvas { position: relative; width: 1200px; height: 900px; }

  .card {
    position: absolute;
    background: var(--paper);
    overflow: hidden;
    box-shadow: 0 10px 30px rgba(0,0,0,.35);
  }

  /* Info side (portrait) */
  .card-info { left: 70px; top: 135px; width: 380px; height: 630px; }
  .card-info .mascot {
    position: absolute; left: 22px; top: 26px; width: 250px; height: 200px;
    border-radius: 14px;
    background: linear-gradient(135deg, var(--mascot-orange) 0%, var(--mascot-orange) 45%, var(--mascot-blue) 100%);
  }
  .card-info .panel {
    position: absolute; left: 0; right: 0; top: 250px; bottom: 0;
    background: linear-gradient(160deg, var(--amber) 0%, var(--amber-deep) 100%);
  }
  .card-info .notch {
    position: absolute; left: 70px; top: 236px; width: 28px; height: 16px;
  }
  .card-info .brand {
    position: absolute; left: 60px; top: 288px;
    font-weight: 800; font-size: 44px; line-height: 1; color: var(--ink);
    letter-spacing: -0.5px;
  }
  .card-info .holder {
    position: absolute; left: 60px; top: 370px;
    font-weight: 700; font-size: 22px; color: var(--ink); letter-spacing: .3px;
  }
  .contact-list {
    position: absolute; left: 60px; top: 425px; list-style: none;
  }
  .contact-list li {
    display: flex; align-items: center; gap: 10px;
    color: var(--paper); font-size: 15px; line-height: 1; margin-bottom: 15px;
  }
  .contact-list svg { width: 14px; height: 14px; flex: none; }

  /* Logo side (landscape) */
  .card-logo { left: 500px; top: 200px; width: 630px; height: 380px; }
  .card-logo .phone {
    position: absolute; left: 230px; top: 48px;
    font-weight: 800; font-size: 46px; color: var(--ink); letter-spacing: 1px;
  }
  .card-logo .tagline {
    position: absolute; left: 232px; top: 112px;
    font-weight: 600; font-size: 19px; color: var(--ink); letter-spacing: 2px;
  }
  .card-logo .mascot {
    position: absolute; left: 40px; top: 60px; width: 160px; height: 150px;
    border-radius: 12px;
    background: linear-gradient(135deg, var(--mascot-orange) 0%, var(--mascot-orange) 45%, var(--mascot-blue) 100%);
  }
  .card-logo .brand {
    position: absolute; left: 180px; top: 200px;
    font-weight: 800; font-size: 72px; line-height: 1; color: var(--ink);
    letter-spacing: -1px;
  }
</style>
</head>
<body>
<div class="canvas">

  <section class="card card-info" aria-label="Info side">
    <div class="mascot" role="img" aria-label="Cartoon handyman mascot in orange overalls and cap giving a thumbs up"></div>
    <div class="panel"></div>
    <svg class="notch" viewBox="0 0 28 16" aria-hidden="true"><polygon points="0,16 28,16 0,0" fill="var(--amber)"/></svg>
    <div class="brand">Tool Baron</div>
    <div class="holder">BORIS LENKOVA</div>
    <ul class="contact-list">
      <li>
        <svg viewBox="0 0 24 24" fill="none" stroke="#fff" stroke-width="2"><path d="M5 3h4l2 5-3 2a11 11 0 0 0 6 6l2-3 5 2v4a2 2 0 0 1-2 2A17 17 0 0 1 3 5a2 2 0 0 1 2-2z"/></svg>
        000 000 0000
      </li>
      <li>
        <svg viewBox="0 0 24 24" fill="none" stroke="#fff" stroke-width="2"><rect x="3" y="5" width="18" height="14"/><path d="M3 5l9 8 9-8"/></svg>
        info@toolbaron.vegas
      </li>
      <li>
        <svg viewBox="0 0 24 24" fill="none" stroke="#fff" stroke-width="2"><circle cx="12" cy="12" r="9"/><path d="M3 12h18M12 3c3 3 3 15 0 18M12 3c-3 3-3 15 0 18"/></svg>
        www.toolbaron.vegas
      </li>
      <li>
        <svg viewBox="0 0 24 24" fill="none" stroke="#fff" stroke-width="2"><path d="M12 22s7-7 7-12a7 7 0 0 0-14 0c0 5 7 12 7 12z"/><circle cx="12" cy="10" r="2.5"/></svg>
        2715 Fenmore Ct, Las Vegas NV 89147
      </li>
    </ul>
  </section>

  <section class="card card-logo" aria-label="Logo side">
    <div class="mascot" role="img" aria-label="Cartoon handyman mascot in orange overalls leaning toward the company name"></div>
    <div class="phone">1 800 000 0000</div>
    <div class="tagline">ONE CALL WE DO IT ALL</div>
    <div class="brand">Tool Baron</div>
  </section>

</div>
</body>
</html>
```